Geschäftspapiere für Kanzlei
Zielgruppe
Forschungsinstitute und Großunternehmen die eigene Entwicklungsabteilungen haben und Erfindungen patentieren lassen.
Aufgabenstellung
Möglicherweise ergibt eine Weiterentwiklung unseres logos Sinn? Denkbar wäre für uns aber auch auf das Logo ganz zu verzichten.
Es sollte nicht mehr als eine Farbe (Blauton) verwendet werden. Wir wollen schlicht, klassisch und seriös auftreten.

```html
<!DOCTYPE html>
<html lang="de">
<head>
<meta charset="utf-8">
<title>Briefbogen Kanzlei Dr. Keladze</title>
<link rel="stylesheet" href="https://fonts.googleapis.com/css2?family=Hind:wght@400;600&display=swap">
<style>
  :root {
    --ink-blue: #0f2d5c;
    --ink-black: #111111;
    --paper: #ffffff;
    --frame: #000000;
  }
  html, body {
    margin: 0;
    padding: 0;
    overflow: hidden;
    background: var(--paper);
  }
  .sheet {
    position: relative;
    width: 848px;
    height: 1200px;
    box-sizing: border-box;
    border: 1px solid var(--frame);
    background: var(--paper);
    font-family: "Hind", sans-serif;
    overflow: hidden;
  }
  .brand {
    position: absolute;
    left: 258px;
    top: 34px;
    display: flex;
    align-items: center;
    gap: 6px;
    color: var(--ink-blue);
    font-size: 13px;
    font-weight: 600;
  }
  .brand-square {
    width: 10px;
    height: 10px;
    background: var(--ink-blue);
  }
  .letterhead {
    position: absolute;
    left: 310px;
    top: 20px;
    color: var(--ink-blue);
    font-size: 13px;
    line-height: 15.4px;
    letter-spacing: 0.5px;
  }
  .letterhead p { margin: 0; }
  .letterhead strong { font-weight: 600; }
  .rule {
    position: absolute;
    height: 0;
    border-top: 1px solid var(--ink-blue);
  }
  .rule-top { left: 119px; width: 610px; top: 93px; }
  .rule-bottom { left: 101px; width: 646px; top: 1145px; }
  .sender-line {
    position: absolute;
    left: 97px;
    top: 180px;
    font-size: 8.6px;
    color: var(--ink-black);
    margin: 0;
  }
  .fold-mark {
    position: absolute;
    left: 0;
    top: 403px;
    width: 12px;
    border-top: 1px solid var(--ink-black);
  }
  .footer {
    position: absolute;
    left: 0;
    right: 0;
    top: 1158px;
    text-align: center;
    color: var(--ink-blue);
    font-size: 10px;
    line-height: 13px;
  }
  .footer p { margin: 0; }
  .footer .titles { font-weight: 600; }
  .sep { padding: 0 4px; }
</style>
</head>
<body>
<main class="sheet">
  <div class="brand" aria-label="Kanzlei Keladze">
    <span class="brand-square"></span>
  </div>
  <header class="letterhead">
    <p><strong>Dr. rer. nat. Tamaz Keladze</strong> PhD</p>
    <p>Patentanwalt</p>
    <p>European Patent Attorney</p>
    <p>European Design- und Trademark Attorney</p>
  </header>
  <div class="rule rule-top"></div>

  <p class="sender-line">Kanzlei Dr. Keladze • Lindenhofstrasse 22 • 80339 München</p>
  <div class="fold-mark"></div>

  <div class="rule rule-bottom"></div>
  <footer class="footer">
    <p class="titles">Dr. rer. nat. Tamaz Keladze, PhD<span class="sep">·</span>Patentanwalt<span class="sep">·</span>European Patent Attorney<span class="sep">·</span>European Design- und Trademark Attorney</p>
    <p>Lindenhofstrasse 22<span class="sep">·</span>80339 München<span class="sep">·</span>Tel. + 49 89 000 412 730<span class="sep">·</span>Fax: + 49 89 000 412 79<span class="sep">·</span>Email: office@keladze-ip.de</p>
  </footer>
</main>
</body>
</html>
```